Multi-Faceted Legal and Finanacial Advisory Group Needs Business Card Design

We need a business card design for a newly branded Orlando Florida area advising group consisting of Attorneys, Accountants and Financial Planners. The company is named RT Counsel Group. You will find our initial work on a business card. The information on the business card are merely guideposts and not final product. The logo does not have the be the same as provided since we have not finalized the logo. We would like to stay with a black/white/grey color scheme, but limited use of color is not out of the question.

Target Market(s)

Businesses and their Corporate Representatives

Industry/Entity Type

Business

Contact Information for Business Card

Should have Name, Title, Phone, Cell, Fax, Email and website. Logo should incorporate RT in some fashion however final logo used does not have to be the one on the document provided.

Requirements
Must have
• An RT design on front and back.

```html
<!DOCTYPE html>
<html lang="en">
<head>
<meta charset="utf-8">
<title>RT Counsel Group – Business Card</title>
<link href="https://fonts.googleapis.com/css2?family=Libre+Baskerville&family=Open+Sans:wght@400;600;800&display=swap" rel="stylesheet">
<style>
  :root {
    --backdrop: #d9d9d9;
    --card-black: #1a1a1a;
    --card-charcoal: #2b2b2b;
    --ink-white: #f4f4f4;
    --ink-grey: #9a9a9a;
    --ink-shadow: #161616;
    --accent-red: #d8262c;
  }
  html, body {
    margin: 0;
    padding: 0;
    overflow: hidden;
  }
  .canvas {
    width: 1200px;
    height: 750px;
    background: var(--backdrop);
    display: flex;
    align-items: center;
    justify-content: center;
    gap: 56px;
  }
  .card {
    position: relative;
    width: 525px;
    height: 300px;
    border-radius: 26px;
    overflow: hidden;
    box-sizing: border-box;
  }
  .card--brand {
    background: linear-gradient(160deg, #333 0%, var(--card-charcoal) 55%, #232323 100%);
  }
  .card--contact {
    background: linear-gradient(150deg, #2a2a2a 0%, var(--card-black) 45%, #0e0e0e 100%);
  }
  .brand-name {
    position: absolute;
    left: 0;
    right: 0;
    top: 104px;
    text-align: center;
    font-family: "Libre Baskerville", Georgia, serif;
    font-size: 30px;
    color: var(--ink-white);
    letter-spacing: 1px;
  }
  .services-line {
    position: absolute;
    left: 0;
    right: 0;
    bottom: 14px;
    text-align: center;
    font-family: "Open Sans", Arial, sans-serif;
    font-weight: 800;
    font-size: 17.5px;
    letter-spacing: 0.5px;
    color: var(--ink-shadow);
    text-transform: uppercase;
  }
  .contact-brand {
    position: absolute;
    right: 40px;
    top: 48px;
    font-family: "Libre Baskerville", Georgia, serif;
    font-size: 24px;
    color: var(--ink-white);
  }
  .person {
    position: absolute;
    left: 34px;
    top: 118px;
    font-family: "Open Sans", Arial, sans-serif;
  }
  .person-name {
    margin: 0;
    font-size: 32px;
    font-weight: 600;
    color: var(--ink-white);
    line-height: 1.05;
  }
  .person-title {
    margin: 0 0 12px;
    font-size: 18px;
    font-weight: 600;
    color: var(--accent-red);
  }
  .contact-list {
    list-style: none;
    margin: 0;
    padding: 0;
    font-size: 11.5px;
    line-height: 1.5;
    color: var(--ink-grey);
  }
  .contact-list .gap {
    margin-top: 6px;
  }
</style>
</head>
<body>
<main class="canvas">
  <section class="card card--brand" aria-label="Card back">
    <div class="brand-name">RT Counsel Group</div>
    <div class="services-line">Attorneys - Accountants - Financial Planners</div>
  </section>

  <section class="card card--contact" aria-label="Card front">
    <div class="contact-brand">RT Counsel Group</div>
    <div class="person">
      <h1 class="person-name">Daniel</h1>
      <p class="person-title">Attorney</p>
      <ul class="contact-list">
        <li>Off: (407) 555-0142</li>
        <li>Cell: (407) 555-0187</li>
        <li>www.rtcounselgroup.com</li>
        <li>daniel@rtcounselgroup.com</li>
        <li class="gap">480 Harbor Park Drive</li>
        <li>Suite 210, Cedar Point, FL 32700</li>
      </ul>
    </div>
  </section>
</main>
</body>
</html>
```